Pelitra needs Brochure Design

we need a brochure design (4 A5 pages, first should be title page with creativity and last should be contact page. 2nd and 3rd should be more informative) for a new company based in Bern, Switzerland called pelitra. We are mobile solution company. We develop mobile apps for different smartphones. we use hybrid technology and browser based technology to develop the apps. we also develop for native platform like Qorbit. Secondly, we develop mobile website, thirdly, we consult company in mobilizing their business. for more details you can see our website www.pelitra-example.com
we would like to see the design which use the three color. two color would be same as the color or our logo, that is, orange and blue and other color could be light aluminium color.

The main message that we want to communicate is that Pelitra would help to the company to mobilize (developing apps, mobile website, mobile marketing, mobile strategy) their business to get the new generation customer. We are innovative, and technologically updates company and cost effective company. ( you can see the text from pelitra website)

The design should reflect a clear and complete message to our viewers.
Updates

Reason: I am travelling and have not enough time to look at design and giving me thoughts. Thank you for understanding.

Please check one design which I design one month before.. this will help to understand the content..

Reason: was delay in communication.. But I am active now and redy to finish this project this week

Reason: less time for feedback..

Reason: personal..

Target Market(s)

The target group is company CEO, Marketing managers of Small to medium size business

Industry/Entity Type

Business

Requirements
Must have
• The orange and blue color must match with the logo of the pelitra
clear and innovative look..
Nice to have
• place the QR code, a feeling of trust and professionalism
Should not have
• not to have too much content written.. not messy ..

```html
<!DOCTYPE html>
<html lang="en">
<head>
<meta charset="utf-8">
<title>Pelitra – Mobile Marketing Brochure Cover</title>
<link href="https://fonts.googleapis.com/css2?family=Comfortaa:wght@700&display=swap" rel="stylesheet">
<style>
  :root {
    --orange: #f7a928;
    --blue: #2a8fe0;
    --white: #ffffff;
    --night: #0c1014;
    --slate: #1d2630;
    --band-top: #05080b;
    --band-bottom-a: #3a2208;
    --band-bottom-b: #6a3e10;
    --frame: #c9ced3;
    --device-body: #0a0c0e;
    --screen-glow: #5a8fb8;
  }
  html, body {
    margin: 0;
    padding: 0;
    overflow: hidden;
    background: #000;
  }
  .cover {
    position: relative;
    width: 846px;
    height: 1200px;
    overflow: hidden;
    font-family: "Comfortaa", "Trebuchet MS", sans-serif;
    font-weight: 700;
    background: radial-gradient(ellipse at 60% 45%, var(--slate) 0%, var(--night) 70%);
  }
  .top-band {
    position: absolute;
    left: 0; top: 0;
    width: 846px; height: 48px;
    background: linear-gradient(180deg, var(--band-top), #10171d);
  }
  .bottom-band {
    position: absolute;
    left: 0; top: 992px;
    width: 846px; height: 208px;
    background: linear-gradient(180deg, var(--band-bottom-b) 0%, var(--band-bottom-a) 55%, #1a0f04 100%);
  }
  .device-art {
    position: absolute;
    left: 67px; top: 75px;
    width: 395px; height: 718px;
    border: 6px solid var(--frame);
    border-radius: 60px;
    background: radial-gradient(ellipse at 45% 48%, var(--screen-glow) 0%, #2c4a63 38%, var(--device-body) 75%);
  }
  .device-reflection {
    position: absolute;
    left: 67px; top: 812px;
    width: 407px; height: 150px;
    border-radius: 0 0 60px 60px;
    background: linear-gradient(180deg, rgba(120,132,142,0.25), rgba(12,16,20,0));
  }
  .tagline {
    position: absolute;
    right: 71px; top: 124px;
    margin: 0;
    text-align: right;
    color: var(--orange);
    font-size: 26px;
    line-height: 38.5px;
  }
  .headline {
    position: absolute;
    left: 300px; top: 330px;
    margin: 0;
    line-height: 1;
  }
  .headline span { display: block; }
  .headline .line-one { color: var(--orange); font-size: 56px; margin-left: 40px; }
  .headline .line-two { color: var(--blue); font-size: 66px; margin-top: 4px; }
  .slogan-line {
    position: absolute;
    left: 400px;
    width: 400px;
    margin: 0;
    text-align: center;
    line-height: 1;
  }
  .slogan-big    { top: 538px; color: var(--orange); font-size: 145px; }
  .slogan-impact { top: 676px; color: var(--blue);   font-size: 60px; }
  .slogan-on     { top: 764px; color: var(--white);  font-size: 50px; }
  .slogan-small  { top: 836px; color: var(--blue);   font-size: 54px; }
  .slogan-screen { top: 866px; color: var(--orange); font-size: 104px; }
  .brand {
    position: absolute;
    left: 0; top: 1070px;
    width: 846px;
    display: flex;
    justify-content: center;
    align-items: center;
    gap: 12px;
  }
  .brand-mark {
    width: 30px; height: 30px;
    background: var(--blue);
  }
  .brand-name {
    color: var(--white);
    font-size: 40px;
    line-height: 1;
  }
</style>
</head>
<body>
  <main class="cover">
    <div class="top-band"></div>
    <div class="bottom-band"></div>

    <div class="device-art" role="img" aria-label="Illustration of a Qorbit smartphone with app icons on its screen and a glowing blue segmented ring"></div>
    <div class="device-reflection" role="img" aria-label="Soft reflection of the smartphone"></div>

    <p class="tagline">take full<br>advantage<br>of mobilized<br>business<br>opportunity</p>

    <h1 class="headline">
      <span class="line-one">mobile</span>
      <span class="line-two">marketing</span>
    </h1>

    <p class="slogan-line slogan-big">big</p>
    <p class="slogan-line slogan-impact">impact</p>
    <p class="slogan-line slogan-on">on</p>
    <p class="slogan-line slogan-small">small</p>
    <p class="slogan-line slogan-screen">screen</p>

    <div class="brand">
      <span class="brand-mark"></span>
      <span class="brand-name">pelitra</span>
    </div>
  </main>
</body>
</html>
```